Boutique Financial Services/Advisor Business Needs Web Design

Looking for an informational and functional web design for my Financial Services/Financial Advisement business. It should have functionality for Company name, address, phone #, "About Us", Who we are, Our Mission, Services we offer, Biographies/Photos of/about "The Team", and possibly a link to "Contact Us". Would like to see something new & exciting blended with a traditional/professional look that will appeal to those approaching retirement, as well as those younger clients that are beginning to think about planning for the future. I already have a web domain through HostMeadow, but would like this to be the design we use for that domain.
Financial Services/Financial Advisor
Coded - Design and coding required
1 page

```html
<!DOCTYPE html>
<html lang="en">
<head>
<meta charset="UTF-8">
<title>Summitline Wealth Management</title>
<link href="https://fonts.googleapis.com/css2?family=Poppins:wght@300;400;500;600;700;800&display=swap" rel="stylesheet">
<style>
:root{
  --navy:#0d0b52;
  --navy-deep:#0a0940;
  --blue:#0b70c0;
  --blue-light:#1b86d6;
  --ink:#111122;
  --body:#3a3a48;
  --muted:#6b6b78;
  --white:#ffffff;
  --grey-soft:#f2f3f6;
}
*{margin:0;padding:0;box-sizing:border-box}
html,body{width:1200px;height:4342px;overflow:hidden}
body{font-family:'Poppins',sans-serif;background:var(--white);color:var(--ink);position:relative}
.abs{position:absolute}
a{text-decoration:none;color:inherit}

/* top bar */
.topbar{position:absolute;left:0;top:0;width:1200px;height:51px;background:var(--navy);color:var(--white)}
.topbar .info{position:absolute;top:10px;display:flex;gap:10px;align-items:center;font-size:11px;line-height:13px}
.topbar .info small{display:block;color:#5fa6e0;font-size:10px}
.topbar .divider{position:absolute;left:988px;top:12px;width:1px;height:26px;background:#4a4a85}
.social{position:absolute;display:flex;gap:16px}
.social span{width:12px;height:12px;border-radius:50%;background:#9a9ac8;display:block}

/* nav */
.nav{position:absolute;top:51px;left:0;width:1200px;height:97px;background:var(--white)}
.nav a{position:absolute;top:44px;font-size:15px;color:#1a1a3a}
.nav a.active{font-weight:600}
.nav .active-mark{position:absolute;left:115px;top:92px;width:44px;height:5px;background:var(--blue);border-radius:3px 3px 0 0}
.brand{position:absolute;text-align:center;color:var(--navy);font-weight:500;letter-spacing:1px;line-height:1.15}
.brand .dot{display:inline-block;width:12px;height:12px;background:var(--navy);margin-bottom:4px}
.btn{position:absolute;background:var(--blue);color:var(--white);font-weight:600;font-size:14px;display:flex;align-items:center;justify-content:center;border-radius:2px}
.btn.navy{background:var(--navy)}

/* hero */
.hero-photo{position:absolute;left:0;top:148px;width:1200px;height:800px;background:linear-gradient(115deg,#233047 0%,#1a2335 35%,#3a4a5e 60%,#5a6c80 80%,#2c3a4d 100%)}
.hero-shade{position:absolute;left:0;top:148px;width:1200px;height:800px;background:linear-gradient(90deg,rgba(6,8,24,.75),rgba(6,8,24,.25) 70%,rgba(6,8,24,.1))}
.hero h1{position:absolute;left:113px;color:var(--white);font-weight:300;font-size:42px;top:312px}
.hero h2{position:absolute;left:112px;color:var(--white);font-weight:700;font-size:60px;top:360px;letter-spacing:.3px}
.hero p{position:absolute;left:118px;top:450px;color:#e6e8ef;font-size:16.5px}

.feature{position:absolute;top:700px;width:313px;height:306px;color:var(--white);text-align:center}
.feature .shape{position:absolute;inset:0}
.feature .icon{position:absolute;left:50%;transform:translateX(-50%);top:100px}
.feature p{position:absolute;left:0;width:100%;top:214px;font-size:17px;line-height:26px}

/* sections */
.label{position:absolute;font-size:16px;letter-spacing:3px;color:var(--ink)}
.heading{position:absolute;font-weight:700;font-size:31px;color:var(--ink);line-height:44px}
.heading .hl{color:var(--blue)}
.para{position:absolute;font-size:13.4px;line-height:25px;color:var(--body)}
.photo{position:absolute}

/* services */
.svc{position:absolute;top:2421px;width:280px;text-align:center;color:var(--white)}
.svc .img{width:280px;height:219px;clip-path:polygon(0 14%,50% 0,100% 14%,100% 100%,0 100%)}
.svc .badge{position:absolute;left:112px;top:194px;width:56px;height:50px;background:var(--blue);clip-path:polygon(0 20%,50% 0,100% 20%,100% 100%,0 100%);border:2px solid #fff}
.svc h3{font-weight:500;font-size:23px;margin-top:32px}
.svc p{font-size:13px;line-height:20px;margin-top:8px;padding:0 20px;color:#dbe8f7}
.arrow-btn{position:absolute;top:2548px;width:34px;height:34px;background:var(--navy);border:1px solid #fff;display:flex;align-items:center;justify-content:center}

/* team */
.member{position:absolute;text-align:center}
.member h4{font-weight:700;font-size:23px;color:var(--ink)}
.member small{font-size:12px;color:var(--muted)}

/* contact */
.field{position:absolute;background:var(--white);font-size:13px;color:#777;padding:14px 24px}

/* footer */
.footer h5{position:absolute;top:4028px;color:var(--white);font-size:17px;font-weight:600}
.footer ul{position:absolute;list-style:none;color:#e5e7f2;font-size:13px}
.footer ul li{height:38.5px}
.contact-item{position:absolute;left:116px;font-size:13px;color:#e5e7f2;line-height:19px}
.contact-item b{display:block;color:var(--blue-light);font-weight:600}
.contact-item svg{position:absolute;left:-24px;top:2px}
</style>
</head>
<body>

<!-- top bar -->
<div class="topbar">
  <div class="info" style="left:107px">
    <svg width="20" height="20" viewBox="0 0 20 20"><circle cx="10" cy="10" r="9" fill="var(--blue)"/><path d="M10 4a4 4 0 0 0-4 4c0 3 4 8 4 8s4-5 4-8a4 4 0 0 0-4-4z" fill="#fff"/></svg>
    <div><small>Location</small>Some Address line goes here</div>
  </div>
  <div class="info" style="left:828px">
    <svg width="22" height="20" viewBox="0 0 22 20"><circle cx="11" cy="10" r="9" fill="var(--blue)"/><path d="M7 6c1 4 4 7 8 8l1.5-2-2.5-1.5-1 1c-1.5-.7-2.5-1.7-3-3l1-1L9.5 5z" fill="#fff"/></svg>
    <div><small style="color:#fff">Phone number</small>123 456 7890</div>
  </div>
  <div class="divider"></div>
  <div class="social" style="left:1009px;top:19px"><span></span><span></span><span></span></div>
</div>

<!-- nav -->
<nav class="nav">
  <a class="active" style="left:115px">Home</a>
  <a style="left:207px">Our Services</a>
  <a style="left:337px">About Us</a>
  <a style="left:808px">Meet the Team</a>
  <div class="active-mark"></div>
  <div class="brand" style="left:470px;top:24px;width:260px;font-size:17px"><span class="dot"></span><br>SUMMITLINE WEALTH<br>MANAGEMENT</div>
</nav>
<a class="btn" style="left:957px;top:79px;width:130px;height:41px">Contact Us</a>

<!-- hero -->
<section class="hero">
  <div class="hero-photo" role="img" aria-label="Advisor's hands reviewing financial documents with a pen at a desk with a laptop"></div>
  <div class="hero-shade"></div>
  <h1>Secure Your Future with</h1>
  <h2>Expert Financial Guidance</h2>
  <p>Tailored solutions for every stage of life—helping you plan, grow, and protect your wealth.</p>
  <a class="btn" style="left:118px;top:509px;width:130px;height:37px;font-size:14px">Contact Us</a>

  <svg class="abs" style="left:0;top:680px" width="1200" height="340" viewBox="0 0 1200 340">
    <polygon points="0,238 600,0 1200,238 1200,340 0,340" fill="var(--blue)"/>
    <polygon points="0,252 600,16 1200,252 1200,340 0,340" fill="var(--white)"/>
  </svg>

  <div class="feature" style="left:111px">
    <svg class="shape" viewBox="0 0 313 306" preserveAspectRatio="none"><polygon points="0,100 313,8 313,306 0,306" fill="var(--navy)"/></svg>
    <svg class="icon" width="80" height="80" viewBox="0 0 80 80" fill="none" stroke="#fff" stroke-width="2.5"><circle cx="28" cy="48" r="18"/><path d="M28 38v20M33 42c-2-2-10-2-10 2s10 2 10 6-8 4-10 2"/><path d="M46 60h28v10H40"/><path d="M56 44c0-12 6-20 16-22-1 10-6 18-16 22zM56 44c-2-8-8-12-14-12 0 7 6 12 14 12z"/></svg>
    <p>Over 10+ years of experience<br>in financial planning.</p>
  </div>
  <div class="feature" style="left:443px;top:666px;height:340px">
    <svg class="shape" viewBox="0 0 314 340" preserveAspectRatio="none"><polygon points="0,70 157,0 314,70 314,340 0,340" fill="var(--blue)"/></svg>
    <svg class="icon" style="top:80px" width="140" height="140" viewBox="0 0 140 140" fill="none" stroke="#fff" stroke-width="3"><circle cx="64" cy="76" r="60"/><circle cx="64" cy="76" r="44"/><circle cx="64" cy="76" r="28"/><circle cx="64" cy="76" r="12"/><path d="M64 76L126 14M108 18l18-4-4 18M114 12v14h14"/></svg>
    <p style="top:248px">Tailored solutions designed<br>to meet your unique goals.</p>
  </div>
  <div class="feature" style="left:777px">
    <svg class="shape" viewBox="0 0 312 306" preserveAspectRatio="none"><polygon points="0,8 312,100 312,306 0,306" fill="var(--navy)"/></svg>
    <svg class="icon" width="84" height="84" viewBox="0 0 84 84" fill="none" stroke="#fff" stroke-width="2.5"><path d="M10 44l16-16 14 6 14-6 16 16-20 20-10-8-10 8z"/><path d="M30 52l8 8M38 46l10 10"/><path d="M60 6l12 4v10c0 8-6 12-12 14-6-2-12-6-12-14V10z"/><path d="M55 18l4 4 7-8"/></svg>
    <p>Trusted by families<br>&amp; businesses</p>
  </div>
</section>

<!-- about -->
<section>
  <svg class="abs" style="left:115px;top:1053px" width="477" height="470" viewBox="0 0 477 470">
    <polygon points="150,0 300,240 0,240" fill="var(--navy)"/>
    <polygon points="0,420 240,385 477,420 477,470 30,470" fill="var(--navy)"/>
  </svg>
  <div class="photo" role="img" aria-label="Senior advisor in a suit seated in a white armchair"
       style="left:115px;top:1160px;width:477px;height:355px;background:linear-gradient(135deg,#e9edf2,#c6cdd6 55%,#8b97a6);clip-path:polygon(0 0,100% 0,100% 100%,50% 86%,0 100%)"></div>
  <div class="label" style="left:627px;top:1160px">About Us</div>
  <div class="heading" style="left:627px;top:1192px;font-size:34px">Our Story</div>
  <p class="para" style="left:627px;top:1251px;width:460px">Summitline Wealth Management was founded with a single goal: to help clients achieve financial independence. Over the years, we've guided individuals, families, and businesses on their journey to secure their financial future. Rooted in trust, transparency, and excellence, we've become a trusted partner for those seeking long-term financial success.</p>
  <a class="btn" style="left:627px;top:1429px;width:130px;height:37px">Read More</a>
</section>

<!-- who we are -->
<section>
  <div class="label" style="left:115px;top:1596px">Who We Are</div>
  <div class="heading" style="left:114px;top:1624px">Experienced Advisors,<br><span class="hl">Committed to Your Success</span></div>
  <p class="para" style="left:115px;top:1719px;width:460px">Summitline Wealth Management was founded with a single goal: to help clients achieve financial independence. Over the years, we've guided individuals, families, and businesses on their journey to secure their financial future. Rooted in trust, transparency, and excellence, we've become a trusted partner for those seeking long-term financial success.</p>
  <svg class="abs" style="left:607px;top:1530px" width="480" height="350" viewBox="0 0 480 350">
    <polygon points="240,0 300,90 180,90" fill="#9a9aa0"/>
    <polygon points="30,340 240,300 450,340 450,350 30,350" fill="var(--navy)"/>
  </svg>
  <div class="photo" role="img" aria-label="Team of colleagues joining hands in a celebratory high five"
       style="left:607px;top:1590px;width:480px;height:280px;background:linear-gradient(120deg,#d9dde3,#8d96a3 45%,#39404c 75%,#aeb4bd);clip-path:polygon(0 8%,50% 0,100% 8%,100% 100%,50% 86%,0 100%)"></div>
</section>

<!-- mission -->
<section>
  <svg class="abs" style="left:111px;top:1899px" width="481" height="350" viewBox="0 0 481 350">
    <polygon points="240,0 300,90 180,90" fill="#9a9aa0"/>
    <polygon points="30,345 240,300 460,345 460,350 30,350" fill="var(--navy)"/>
  </svg>
  <div class="photo" role="img" aria-label="Advisors pointing at stock market charts on a large screen"
       style="left:111px;top:1960px;width:481px;height:285px;background:linear-gradient(110deg,#1d5fb0,#6e9ad0 40%,#dfe6ee 65%,#2c3e5a);clip-path:polygon(0 10%,50% 0,100% 10%,100% 100%,50% 84%,0 100%)"></div>
  <div class="label" style="left:625px;top:2000px">Our Mission</div>
  <div class="heading" style="left:624px;top:2027px">Guiding You to Your<br><span class="hl">Financial Summit</span></div>
  <p class="para" style="left:625px;top:2130px;width:470px">Our mission is simple yet powerful: to equip our clients with the knowledge, tools, and strategies to achieve their financial dreams. Through personalized service and dedicated support, we aim to help you reach the peak of financial confidence.</p>
</section>

<!-- services -->
<section>
  <div class="label" style="left:0;width:1200px;text-align:center;top:2301px">Services We Offer</div>
  <div class="heading" style="left:0;width:1200px;text-align:center;top:2330px">Comprehensive <span class="hl">Financial Solutions</span></div>
  <svg class="abs" style="left:0;top:2390px" width="1200" height="540" viewBox="0 0 1200 540">
    <polygon points="0,154 600,0 1200,154 1200,512 600,390 0,512" fill="var(--blue)"/>
    <polygon points="30,532 600,400 1175,532 1175,540 600,418 30,540" fill="var(--navy)"/>
  </svg>
  <div class="abs" style="left:443px;top:2544px;width:314px;height:287px;background:var(--navy)"></div>

  <div class="svc" style="left:130px">
    <div class="img" role="img" aria-label="Advisor's hands above rising investment charts" style="background:linear-gradient(160deg,#1c2a44,#0f1a30 60%,#2e6fb0)"></div>
    <div class="badge"></div>
    <h3>Investment Management</h3>
    <p>Grow and preserve your wealth through expert portfolio management.</p>
  </div>
  <div class="svc" style="left:460px">
    <div class="img" role="img" aria-label="Tax planning notebook with checklist and pen" style="background:linear-gradient(150deg,#e8e2d6,#cdbfa6 50%,#f2efe9)"></div>
    <div class="badge"></div>
    <h3>Tax Planning</h3>
    <p>Minimize liabilities and maximize your savings</p>
  </div>
  <div class="svc" style="left:790px">
    <div class="img" role="img" aria-label="Protective hands surrounding insurance icons" style="background:linear-gradient(160deg,#1a2536,#0e1726 60%,#23578f)"></div>
    <div class="badge"></div>
    <h3>Insurance Solutions</h3>
    <p>Mitigate risk and safeguard what matters most.</p>
  </div>
  <a class="abs" style="left:550px;top:2778px;color:#fff;font-size:13px;font-weight:600;display:flex;gap:10px;align-items:center">Read More <span style="width:20px;height:18px;background:var(--blue);display:flex;align-items:center;justify-content:center"><svg width="10" height="8" viewBox="0 0 10 8"><path d="M0 4h8M5 1l3 3-3 3" stroke="#fff" fill="none" stroke-width="1.5"/></svg></span></a>
  <div class="arrow-btn" style="left:110px"><svg width="10" height="8" viewBox="0 0 10 8"><path d="M10 4H2M5 1L2 4l3 3" stroke="#fff" fill="none" stroke-width="1.5"/></svg></div>
  <div class="arrow-btn" style="left:1062px"><svg width="10" height="8" viewBox="0 0 10 8"><path d="M0 4h8M5 1l3 3-3 3" stroke="#fff" fill="none" stroke-width="1.5"/></svg></div>
</section>

<!-- team -->
<section>
  <div class="label" style="left:0;width:1200px;text-align:center;top:2893px">Meet The Team</div>
  <div class="heading" style="left:0;width:1200px;text-align:center;top:2912px">Our Trusted <span class="hl">Advisors</span></div>
  <svg class="abs" style="left:0;top:2990px" width="1200" height="340" viewBox="0 0 1200 340">
    <polygon points="0,120 600,0 1200,120 1200,170 600,50 0,170" fill="var(--grey-soft)"/>
    <polygon points="0,230 600,110 1200,230 1200,280 600,160 0,280" fill="var(--grey-soft)"/>
    <polygon points="423,50 423,340 360,340" fill="var(--navy)"/>
    <polygon points="1009,50 1009,340 950,340" fill="var(--navy)"/>
    <polygon points="473,60 600,10 726,60 726,340 473,340" fill="var(--blue)"/>
  </svg>
  <div class="photo" role="img" aria-label="Portrait of Owen Hartley in a grey suit" style="left:190px;top:3000px;width:233px;height:328px;background:linear-gradient(180deg,rgba(255,255,255,0) 0%,#b9bcc2 35%,#6d7380 80%,#1a1e5c);clip-path:polygon(20% 0,80% 0,100% 40%,100% 100%,0 100%,0 40%)"></div>
  <div class="photo" role="img" aria-label="Portrait of Marcus Ellery in a dark suit" style="left:473px;top:2966px;width:253px;height:362px;background:linear-gradient(180deg,rgba(255,255,255,0) 0%,#8f98a6 30%,#2a2f3c 75%,#141a4a);clip-path:polygon(25% 0,75% 0,100% 35%,100% 100%,0 100%,0 35%)"></div>
  <div class="photo" role="img" aria-label="Portrait of Calvin Brooks in a checked blazer" style="left:777px;top:3000px;width:232px;height:328px;background:linear-gradient(180deg,rgba(255,255,255,0) 0%,#a3a8b2 35%,#5d6472 80%,#1a1e5c);clip-path:polygon(20% 0,80% 0,100% 40%,100% 100%,0 100%,0 40%)"></div>
  <div class="member" style="left:190px;top:3346px;width:250px;margin-left:-9px"><h4>Owen Hartley</h4><small>Senior Financial Planner</small></div>
  <div class="member" style="left:474px;top:3346px;width:250px"><h4>Marcus Ellery</h4><small>Founder &amp; Chief Financial Officer</small></div>
  <div class="member" style="left:760px;top:3346px;width:250px;margin-left:3px"><h4>Calvin Brooks</h4><small>Client Relations Specialist</small></div>
</section>

<!-- contact -->
<section>
  <svg class="abs" style="left:0;top:3425px" width="1200" height="520" viewBox="0 0 1200 520">
    <polygon points="250,90 600,4 950,90 950,140 250,140" fill="var(--navy)"/>
    <polygon points="168,130 600,30 1031,130 1031,500 168,500" fill="var(--blue)"/>
    <polygon points="0,462 168,430 168,460 0,480" fill="var(--blue)"/>
    <polygon points="1200,462 1031,430 1031,460 1200,480" fill="var(--blue)"/>
  </svg>
  <div class="heading" style="left:0;width:1200px;text-align:center;top:3530px;color:#fff;font-size:28px">Get In Touch With Us</div>
  <div class="field" style="left:256px;top:3599px;width:334px;height:47px">Full Name</div>
  <div class="field" style="left:610px;top:3599px;width:334px;height:47px">Email</div>
  <div class="field" style="left:256px;top:3660px;width:688px;height:93px;padding-top:12px">Message</div>
  <a class="btn navy" style="left:534px;top:3768px;width:132px;height:37px">Read More</a>
</section>

<!-- footer -->
<footer class="footer">
  <div class="abs" style="left:0;top:3905px;width:1200px;height:437px;background:var(--navy)"></div>
  <svg class="abs" style="left:0;top:3860px" width="1200" height="50" viewBox="0 0 1200 50">
    <polygon points="0,30 168,0 168,50 0,50" fill="var(--navy)"/>
    <polygon points="1200,30 1031,0 1031,50 1200,50" fill="var(--navy)"/>
  </svg>
  <div class="brand" style="left:470px;top:3880px;width:260px;font-size:17px;color:#fff"><span class="dot" style="background:#fff"></span><br>SUMMITLINE WEALTH<br>MANAGEMENT</div>

  <h5 style="left:116px">Contact Info</h5>
  <div class="contact-item" style="top:4077px">
    <svg width="14" height="12" viewBox="0 0 14 12"><rect x="1" y="1" width="12" height="10" fill="none" stroke="#1b86d6" stroke-width="1.5"/><path d="M1 1l6 5 6-5" fill="none" stroke="#1b86d6" stroke-width="1.5"/></svg>
    <b>Email Address</b>info@summitlinewealth.com</div>
  <div class="contact-item" style="top:4134px">
    <svg width="14" height="14" viewBox="0 0 14 14"><path d="M2 1c1 6 5 10 11 11l1-3-3-2-1.5 1.5C7.5 7.5 6.5 6.5 5.5 5L7 3.5 5 1z" fill="#1b86d6"/></svg>
    <b>Phone Number</b>123 456 7890</div>
  <div class="contact-item" style="top:4192px">
    <svg width="12" height="15" viewBox="0 0 12 15"><path d="M6 1a5 5 0 0 0-5 5c0 4 5 8 5 8s5-4 5-8a5 5 0 0 0-5-5z" fill="none" stroke="#1b86d6" stroke-width="1.5"/></svg>
    <b>Location</b>Some Address Line<br>Goes Here</div>

  <h5 style="left:391px">Quick Links</h5>
  <ul style="left:391px;top:4078px"><li>Home</li><li>About Us</li><li>Meet Our Team</li><li>Contact Us</li></ul>

  <h5 style="left:608px">Our Services</h5>
  <ul style="left:608px;top:4078px"><li>Retirement Planning</li><li>Investment Management</li><li>Tax Planning</li><li>Estate Planning</li><li>Insurance Solutions</li></ul>

  <h5 style="left:843px">Subscribe To A Newsletter</h5>
  <div class="abs" style="left:843px;top:4078px;width:244px;height:42px;background:#fff;border:2px solid var(--blue);font-size:11px;color:#888;padding:12px 14px">Enter your email</div>
  <div class="btn" style="left:994px;top:4080px;width:91px;height:38px;font-size:12px;font-weight:500;border-radius:0">Subscribe</div>
  <div class="social" style="left:1028px;top:4145px;gap:20px"><span style="width:16px;height:16px;background:#fff"></span><span style="width:16px;height:16px;background:#fff"></span></div>

  <div class="abs" style="left:88px;top:4276px;width:974px;height:1px;background:#2b2a72"></div>
  <div class="abs" style="left:0;top:4302px;width:1200px;text-align:center;color:#e5e7f2;font-size:13px">Copyright © Summitline Wealth Management. All Rights Reserved.</div>
</footer>

</body>
</html>
```